GPS Tracker Business Card Design

We need a business card for a GPS Vehicle tracking company. We sell the hardware for the vehicle and the software platform to monitor your vehicle/s. Including high asset non-powered vehicles like a trailer using our solar powered unit.
We like using dark blue to different shades of blue along with gold. We have phone apps for Android and Apple devices.

We have a platform for families wanting to track their teenage driver and children; Plus a Fleet vehicle tracking platform.

Features: unlimited number of vehicles and/or assets including snow mobiles forklifts generators trailers airport equipment

Reports for driving behavior reports and alerts dashboard fleet maintenace timeline view and replay geofence real time alerts logbook scheduling route optimization accounting integration fleet grouping closest vehicle locator On Board Diagnostics.

Benefits: Increased productivity improved fuel efficiency organizing your business improve time management simplify back end processes, reduce fleet fuel efficiency and expenses increase fleet security etc..

Please view website: Velmora.com

Industry/Entity Type

Business

Contact Information for Business Card

Harold B Pennick

```html
<!DOCTYPE html>
<html lang="en">
<head>
<meta charset="utf-8">
<title>Velmora Business Card</title>
<link href="https://fonts.googleapis.com/css2?family=Open+Sans:wght@300;400;600;700&display=swap" rel="stylesheet">
<style>
  :root {
    --navy: #101f5c;
    --navy-deep: #0b1649;
    --blue: #1d7fd6;
    --paper: #f4f4f4;
    --paper-shade: #e4e4e4;
    --ink: #141414;
    --grey: #8a8a8a;
    --tag-light: #9aa3c4;
    --backdrop: #dcd8d0;
    --rule: rgba(255,255,255,0.85);
  }
  * { box-sizing: border-box; margin: 0; padding: 0; }
  html, body { width: 1200px; height: 780px; overflow: hidden; }
  body {
    background: var(--backdrop);
    font-family: "Open Sans", Arial, sans-serif;
    display: flex;
    align-items: center;
    justify-content: center;
    gap: 40px;
  }
  .card {
    width: 540px;
    height: 309px;
    position: relative;
    overflow: hidden;
    box-shadow: 0 8px 24px rgba(0,0,0,0.18);
  }
  .brand-name {
    font-weight: 300;
    font-size: 62px;
    letter-spacing: -1px;
    line-height: 1;
    white-space: nowrap;
  }
  .tagline {
    font-weight: 400;
    font-size: 17px;
    margin-top: 6px;
    letter-spacing: 0.3px;
    white-space: nowrap;
  }

  /* ---------- Front ---------- */
  .card--front { background: var(--navy); }
  .front__visual {
    position: absolute; inset: 0 0 auto 0; height: 160px;
    background: radial-gradient(ellipse at 65% 40%, #2c4394 0%, #18287a 45%, var(--navy) 100%);
  }
  .front__brand { position: absolute; left: 34px; top: 44px; }
  .front__brand .brand-name { color: var(--paper); }
  .front__brand .tagline { color: var(--tag-light); }
  .front__band {
    position: absolute; left: 0; right: 0; top: 160px; height: 94px;
    background: linear-gradient(180deg, var(--paper) 0%, var(--paper-shade) 100%);
    display: flex; align-items: center;
    padding: 0 28px 0 30px;
  }
  .front__band::before, .front__band::after {
    content: ""; position: absolute; left: 0; right: 0; height: 1px; background: var(--rule);
  }
  .front__band::before { top: -5px; }
  .front__band::after { bottom: -5px; }
  .person { width: 210px; }
  .person__name { font-size: 21px; font-weight: 400; color: var(--ink); white-space: nowrap; }
  .person__title { font-size: 16px; color: var(--blue); margin-top: 2px; }
  .divider { width: 1px; height: 58px; background: #9a9a9a; margin: 0 18px; }
  .contacts { list-style: none; font-size: 14.5px; color: var(--ink); line-height: 1.45; }
  .contacts li { display: flex; align-items: center; gap: 8px; white-space: nowrap; }
  .contacts svg { width: 15px; height: 15px; flex: none; }
  .front__web {
    position: absolute; left: 0; right: 0; bottom: 0; height: 55px;
    display: flex; align-items: center; padding-left: 150px;
    color: var(--blue); font-size: 16px;
  }

  /* ---------- Back ---------- */
  .card--back { background: linear-gradient(160deg, #fbfbfb 0%, var(--paper-shade) 100%); }
  .back__brand { position: absolute; right: 58px; top: 36px; }
  .back__brand .brand-name { color: var(--ink); font-size: 60px; }
  .back__brand .tagline { color: var(--grey); }
  .back__band {
    position: absolute; left: 0; right: 0; top: 150px; height: 110px;
    background: var(--navy);
    padding: 14px 22px 0 22px;
    color: #fff;
  }
  .back__band::before, .back__band::after {
    content: ""; position: absolute; left: 0; right: 0; height: 1px; background: var(--navy-deep);
  }
  .back__band::before { top: -5px; }
  .back__band::after { bottom: -5px; }
  .benefits__title { font-size: 18px; font-weight: 600; text-align: right; margin-bottom: 6px; }
  .benefits__text { font-size: 12.5px; line-height: 1.35; }
  .back__web {
    position: absolute; left: 22px; bottom: 12px;
    color: var(--blue); font-size: 15px;
  }
</style>
</head>
<body>

  <section class="card card--front" aria-label="Business card front">
    <div class="front__visual" role="img" aria-label="Faint illustration of a world map with location markers and people"></div>
    <div class="front__brand">
      <div class="brand-name">Velmora</div>
      <div class="tagline">Every Road, Every Mile</div>
    </div>
    <div class="front__band">
      <div class="person">
        <div class="person__name">Harold B Pennick</div>
        <div class="person__title">Owner</div>
      </div>
      <div class="divider"></div>
      <ul class="contacts">
        <li>
          <svg viewBox="0 0 16 16"><rect width="16" height="16" rx="2" fill="#1d7fd6"/><path d="M5 3.5l2 2-1 1.3c.6 1.3 1.5 2.2 2.8 2.8L10 8.6l2 2-1.3 1.6C7.5 11.8 4.3 8.6 3.9 5.2z" fill="#fff"/></svg>
          866-555-0142
        </li>
        <li>
          <svg viewBox="0 0 16 16"><rect width="16" height="16" rx="2" fill="#1d7fd6"/><rect x="3" y="4.5" width="10" height="7" fill="none" stroke="#fff" stroke-width="1.2"/><path d="M3 4.8l5 4 5-4" fill="none" stroke="#fff" stroke-width="1.2"/></svg>
          hello@velmora.com
        </li>
        <li>
          <svg viewBox="0 0 16 16"><rect width="16" height="16" rx="2" fill="#1d7fd6"/><circle cx="8" cy="8" r="4.8" fill="none" stroke="#fff" stroke-width="1.1"/><ellipse cx="8" cy="8" rx="2" ry="4.8" fill="none" stroke="#fff" stroke-width="1"/><path d="M3.2 8h9.6" stroke="#fff" stroke-width="1"/></svg>
          www.velmora.com
        </li>
      </ul>
    </div>
    <div class="front__web">www.velmora.com</div>
  </section>

  <section class="card card--back" aria-label="Business card back">
    <div class="back__brand">
      <div class="brand-name">Velmora</div>
      <div class="tagline">Every Road, Every Mile</div>
    </div>
    <div class="back__band">
      <h2 class="benefits__title">Benefits</h2>
      <p class="benefits__text">Increased productivity improved fuel efficiency organizing your business improve time management simplify back end processes, reduce fleet fuel efficiency and expenses increase fleet security etc..</p>
    </div>
    <div class="back__web">www.velmora.com</div>
  </section>

</body>
</html>
```